Trucking company specializing in intermodal containers

We need a logo design for our trucking company based in Kent, Washington. Our companies name is Varnell Haulways LLC, we specialize in intermodal containers, and work off of the Crestmark Rail Lines and the ports. We provide service by transporting freight with our fleet of trucks. We operate within Washington, Oregon, and Idaho. Our fleet consists of an east division and a local division. Our team motto currently is globally connected, locally invested.

Target Market(s)

brokers, intermodal management companies, customers

Industry/Entity Type

Trucking Company

Contact Information for Business Card

physical address 4153 N. 318th Pl Kent, WA 98417
office number is 253-555-0148

Font styles to use
Sans Serif

Colors

Designer to choose colors to be used in the design.

Requirements
Must have
• We need to update our current logo. Something like an emblem; that makes a statement that this logo/ sign represents Varnell Haulways. Something like a royal stamp but in this case a royal shield.
Nice to have
• simple, yet bold. something someone does not currently have. We need something fresh and exciting. Something that will also make a statement because currently our reputation is great within the industry and our community. But we need to reflect that we are professional and willing to provide the best service. We are open to new statement lines.
Should not have
• Should not have something thats been used before. We are open to suggestions that you have and a design that is completely unique and you make originally without what we want but what you like as well. Ofcourse it should still represent the industry we are in.

```html
<!DOCTYPE html>
<html lang="en">
<head>
<meta charset="utf-8">
<title>Varnell Haulways LLC – Business Card</title>
<link href="https://fonts.googleapis.com/css2?family=Lato:wght@400;700;900&family=Alegreya:wght@700&display=swap" rel="stylesheet">
<style>
  :root {
    --maroon: #8e0f10;
    --orange: #eea00a;
    --ink: #2b2b2b;
    --card: #ffffff;
    --backdrop: #e9e6e2;
    --rule: #d98a06;
  }
  * { box-sizing: border-box; margin: 0; padding: 0; }
  html, body {
    width: 1200px; height: 900px; overflow: hidden;
    background: var(--backdrop);
  }
  .card {
    position: absolute;
    left: 110px; top: 170px;
    width: 980px; height: 560px;
    background: var(--card);
    overflow: hidden;
    box-shadow: 0 10px 30px rgba(0,0,0,.12);
    font-family: "Lato", sans-serif;
    color: var(--ink);
  }
  .brand {
    position: absolute; left: 56px; top: 82px;
    display: flex; align-items: center; gap: 18px;
  }
  .brand-mark {
    width: 26px; height: 26px; background: var(--maroon);
  }
  .brand-name {
    font-family: "Lato", sans-serif;
    font-weight: 900;
    font-size: 38px;
    line-height: 1.05;
    color: var(--maroon);
    text-transform: uppercase;
    letter-spacing: .5px;
  }
  .person { position: absolute; left: 54px; top: 322px; }
  .person-name {
    font-family: "Alegreya", serif;
    font-weight: 700;
    font-size: 32px;
    color: var(--maroon);
    letter-spacing: .5px;
  }
  .person-title { font-size: 24px; margin-top: 2px; }
  .contacts { position: absolute; left: 54px; top: 453px; list-style: none; }
  .contacts li {
    display: flex; align-items: center; gap: 12px;
    font-size: 24px; height: 36px;
  }
  .contacts svg { width: 20px; height: 20px; fill: var(--maroon); flex: none; }
  .cab-art { position: absolute; left: 573px; top: 0; width: 407px; height: 560px; }
  .address {
    position: absolute; right: 52px; top: 238px;
    text-align: right; color: #fff;
    font-size: 25px; line-height: 1.4;
  }
  .address-rule {
    position: absolute; right: 0; top: 325px;
    width: 250px; height: 1px; background: var(--rule);
  }
</style>
</head>
<body>
  <div class="card">
    <div class="brand">
      <span class="brand-mark"></span>
      <div class="brand-name">Varnell Haulways<br>LLC</div>
    </div>

    <div class="person">
      <div class="person-name">MARCUS DELANEY</div>
      <div class="person-title">Managing Director</div>
    </div>

    <ul class="contacts">
      <li>
        <svg viewBox="0 0 24 24"><path d="M6.6 10.8a15.1 15.1 0 0 0 6.6 6.6l2.2-2.2a1 1 0 0 1 1-.25 11.4 11.4 0 0 0 3.6.57 1 1 0 0 1 1 1V20a1 1 0 0 1-1 1A17 17 0 0 1 3 4a1 1 0 0 1 1-1h3.5a1 1 0 0 1 1 1c0 1.25.2 2.45.57 3.6a1 1 0 0 1-.25 1z"/></svg>
        253-555-0148
      </li>
      <li>
        <svg viewBox="0 0 24 24"><path d="M2 5h20v14H2z" fill="none"/><path d="M2 6l10 7 10-7v12H2z"/><path d="M2 5h20l-10 7z"/></svg>
        info@varnellhaulways.com
      </li>
      <li>
        <svg viewBox="0 0 24 24"><circle cx="12" cy="12" r="10"/><path d="M2 12h20M12 2c3 3 3 17 0 20M12 2c-3 3-3 17 0 20" stroke="#fff" stroke-width="1.4" fill="none"/></svg>
        www.varnellhaulways.com
      </li>
    </ul>

    <svg class="cab-art" viewBox="0 0 407 560" role="img" aria-label="Stylized orange truck cab in side view">
      <path d="M60 0 H407 V560 H0 V470 Q0 440 30 430 L60 420 Z" fill="var(--orange)"/>
    </svg>

    <div class="address">4153 N. 318th<br>Pl Kent, WA 98417</div>
    <div class="address-rule"></div>
  </div>
</body>
</html>
```